nestlybloom - Ballon Design

I need a Ballon designed. Please use the psb file ballon_template.psb as template.

I would like to have a ballon designed similar to the file "example.png".
instead of the lorna kin logo please use my attached logo "nestlybloom logo.ai"

The text should be the same " IT'S A MOM" but the logo should be different.

I should look like more elegant. should be also white background. But for the design feel free.

thanks.
Updates

Please also add the webpage "www.nestlybloom.eu" on the ballon design.

```html
<!DOCTYPE html>
<html lang="en">
<head>
<meta charset="utf-8">
<title>nestlybloom – It's a Mom balloon</title>
<link rel="stylesheet" href="https://fonts.googleapis.com/css2?family=Playfair+Display:wght@800&family=Montserrat:wght@600&display=swap">
<style>
  :root {
    --backdrop: #e4e4e6;
    --balloon: #ffffff;
    --balloon-edge: #ececee;
    --pink: #e47aad;
    --pink-soft: #d2679b;
    --navy: #2742a0;
  }
  html, body {
    margin: 0;
    padding: 0;
    width: 1200px;
    height: 789px;
    overflow: hidden;
    background: var(--backdrop);
  }
  .canvas {
    position: relative;
    width: 1200px;
    height: 789px;
    display: flex;
    align-items: center;
    justify-content: center;
  }
  .balloon-face {
    width: 680px;
    height: 680px;
    border-radius: 50%;
    background: var(--balloon);
    box-shadow: 0 0 0 6px var(--balloon-edge);
    display: flex;
    flex-direction: column;
    align-items: center;
    justify-content: center;
    text-align: center;
  }
  .headline {
    margin: 0;
    font-family: "Playfair Display", Georgia, serif;
    font-weight: 800;
    color: var(--pink);
    font-size: 140px;
    line-height: 0.86;
    letter-spacing: -2px;
    text-transform: uppercase;
  }
  .headline span { display: block; }
  .brand {
    margin-top: 44px;
    display: flex;
    flex-direction: column;
    align-items: center;
  }
  .brand-name {
    font-family: "Playfair Display", Georgia, serif;
    font-weight: 800;
    font-size: 44px;
    line-height: 1;
    color: var(--navy);
  }
  .brand-web {
    margin-top: 8px;
    font-family: "Montserrat", Arial, sans-serif;
    font-weight: 600;
    font-size: 19px;
    letter-spacing: 0.5px;
    color: var(--pink-soft);
  }
</style>
</head>
<body>
  <main class="canvas">
    <section class="balloon-face">
      <h1 class="headline">
        <span>It's</span>
        <span>A</span>
        <span>Mom</span>
      </h1>
      <div class="brand">
        <span class="brand-name">nestlybloom</span>
        <span class="brand-web">www.nestlybloom.eu</span>
      </div>
    </section>
  </main>
</body>
</html>
```